Business Cards

We were billed for this because the project timed out. Please give me another designed to open this back up. I was not happy with the last designs (that I was charged for).
we are also using the logo with Revitalizing Pools One Drop at a Time
Also want to utilize Where Healthy Water is our Commitment.

Contact Information for Business Card

Marlowe Stone Group Inc

```html
<!DOCTYPE html>
<html lang="en">
<head>
<meta charset="utf-8">
<title>Marlowe Stone Group – Business Card</title>
<link href="https://fonts.googleapis.com/css2?family=Montserrat:wght@400;500;700&display=swap" rel="stylesheet">
<style>
  :root{
    --page-bg:#d9d9d9;
    --card-white:#fdfdfd;
    --wordmark-grey:#5a5a5a;
    --blue-light:#5c97c6;
    --blue-deep:#1262a5;
    --band-cyan:#1db3e2;
    --band-cyan-light:#45c4ea;
    --text-white:#ffffff;
  }
  *{box-sizing:border-box;margin:0;padding:0}
  html,body{width:1200px;height:1200px;overflow:hidden}
  body{
    background:var(--page-bg);
    font-family:"Montserrat",sans-serif;
    display:flex;flex-direction:column;align-items:center;justify-content:center;gap:56px;
  }
  .card{
    width:760px;height:434px;border-radius:26px;position:relative;overflow:hidden;
    box-shadow:0 6px 18px rgba(0,0,0,.18);
  }
  /* Front */
  .card-front{background:var(--card-white);display:flex;align-items:center;justify-content:center}
  .front-name{
    font-weight:700;font-size:42px;letter-spacing:4px;color:var(--wordmark-grey);text-transform:uppercase;
  }
  /* Back */
  .card-back{background:linear-gradient(100deg,var(--blue-light) 0%,var(--blue-deep) 52%,var(--blue-deep) 100%)}
  .back-mark{
    position:absolute;top:44px;right:48px;
    font-weight:700;font-size:22px;letter-spacing:1px;color:var(--text-white);
  }
  .details{
    position:absolute;top:146px;left:0;right:0;
    display:flex;align-items:center;justify-content:center;gap:26px;color:var(--text-white);
  }
  .person{text-align:right}
  .person-name{font-weight:700;font-size:40px;line-height:1.1}
  .person-title{font-weight:400;font-size:20px;margin-top:6px}
  .divider{width:2px;height:104px;background:var(--text-white);opacity:.85}
  .contact-list{list-style:none;display:flex;flex-direction:column;gap:8px}
  .contact-item{display:flex;align-items:center;gap:12px;font-size:20px;font-weight:400}
  .contact-icon{width:18px;height:18px;flex:none}
  .address-band{
    position:absolute;left:0;right:0;bottom:0;height:76px;
    background:linear-gradient(90deg,var(--band-cyan-light),var(--band-cyan));
    display:flex;align-items:center;justify-content:center;
    color:var(--text-white);font-size:22px;font-weight:500;letter-spacing:.5px;
  }
</style>
</head>
<body>
  <section class="card card-front">
    <h1 class="front-name">Marlowe Stone Group</h1>
  </section>

  <section class="card card-back">
    <div class="back-mark">Marlowe Stone Group</div>
    <div class="details">
      <div class="person">
        <p class="person-name">Dorian Vale</p>
        <p class="person-title">Founder &amp; Director</p>
      </div>
      <div class="divider"></div>
      <ul class="contact-list">
        <li class="contact-item">
          <svg class="contact-icon" viewBox="0 0 24 24" fill="#fff"><path d="M6.6 10.8a15 15 0 0 0 6.6 6.6l2.2-2.2c.3-.3.7-.4 1-.2 1.1.4 2.3.6 3.6.6.6 0 1 .4 1 1V20c0 .6-.4 1-1 1A17 17 0 0 1 3 4c0-.6.4-1 1-1h3.5c.6 0 1 .4 1 1 0 1.3.2 2.5.6 3.6.1.3 0 .7-.2 1z"/></svg>
          <span>(405)-555-0147</span>
        </li>
        <li class="contact-item">
          <svg class="contact-icon" viewBox="0 0 24 24" fill="#fff"><path d="M2 5h20v14H2z M3.5 6.5 12 13l8.5-6.5" stroke="#1262a5" stroke-width="1.6"/></svg>
          <span>vale@marlowestonegroup.com</span>
        </li>
        <li class="contact-item">
          <svg class="contact-icon" viewBox="0 0 24 24" fill="none" stroke="#fff" stroke-width="2"><circle cx="12" cy="12" r="9"/><path d="M3 12h18M12 3c3 3 3 15 0 18M12 3c-3 3-3 15 0 18"/></svg>
          <span>www.marlowestonegroup.com</span>
        </li>
      </ul>
    </div>
    <div class="address-band">4870 Harbor Lane Fairhaven Maine 04120</div>
  </section>
</body>
</html>
```